Tech Tradeshow Brochure Design Project

Our tech recruiting firm in NYC is looking for a modern new pamphlet for an upcoming tech trade show. We've been in business for 25 years, which is most likely how long its been since we ever updated our brochures. Regardless, we're busy placing programmers and software engineers and need a new brochure design, perhaps a creative one in the shape of our logo which is a power button. We're in the middle of updating and modernizing our look which you can reference in our logo and a screenshot of our re-skinned website homepage.

We'd like something that uses the blue and green colors and caters to both professionals looking for tech jobs as well as young programmers who want to work in a start up firm. The final design should communicate approachable, modern technology recruitment services.
Updates

Hi Designers,

Looking forward to seeing the great work coming soon! I wanted to provide an update regarding the pamphlet length. We'd like to see use of a fun, innovative shape (as opposed to a basic rectangular shape) and the content would end up being about 3-4 pages. Hope this clarifies and please see the attached files for the use of logos. Thank you!

Hi all,

Have attached a PDF of the brochure text & content, if you'd like to include it within the design. Thank you very much. 

Target Market(s)

Software engineers, clients from companies looking to place talent

Industry/Entity Type

Software

Requirements
Must have
• -Must have our logo and slogan: Powering tech careers for 25 years.
-Include the text of the PDF.
Nice to have
• Must utilize our colors and be visually stimulating

```html
<!DOCTYPE html>
<html lang="en">
<head>
<meta charset="utf-8">
<title>Kestrel Brochure Inside Spread</title>
<link rel="stylesheet" href="https://fonts.googleapis.com/css2?family=Mulish:wght@400;600&family=Nunito:wght@600;800&family=Shadows+Into+Light+Two&display=swap">
<style>
  :root {
    --navy: #1f3566;
    --green: #8db859;
    --ink: #2a2a2a;
    --grey: #4a4a4a;
    --paper: #ffffff;
  }
  * { margin: 0; padding: 0; box-sizing: border-box; }
  html, body { width: 1200px; height: 928px; overflow: hidden; background: var(--paper); }
  .spread { position: relative; width: 1200px; height: 928px; background: var(--paper); font-family: "Mulish", sans-serif; color: var(--ink); }

  .band { position: absolute; left: 0; width: 1200px; height: 13px; background: var(--green); }
  .band--top { top: 0; }
  .band--bottom { bottom: 0; }
  .tab { position: absolute; left: 843px; width: 315px; background: var(--green); }
  .tab--top { top: 0; height: 67px; border-radius: 0 0 14px 14px; }
  .tab--bottom { top: 861px; height: 55px; border-radius: 14px 14px 0 0; }

  .body-copy p { font-size: 19.5px; line-height: 28px; text-align: justify; margin-bottom: 11px; }

  .about { position: absolute; left: 43px; top: 57px; width: 314px; }
  .about__label { background: var(--navy); color: var(--paper); border-radius: 6px; height: 52px; font-family: "Nunito", sans-serif; font-weight: 800; font-size: 32px; line-height: 52px; text-align: center; margin-bottom: 18px; }

  .art { position: absolute; border-radius: 14px; background: linear-gradient(160deg, #dfe6f1, #f1f4f9); }
  .art--bubbles { left: 470px; top: 60px; width: 162px; height: 176px; border-radius: 50%; }
  .art--figure { left: 414px; top: 218px; width: 112px; height: 110px; background: linear-gradient(160deg, #e4e8ef, #f4f6f9); }
  .tagline { position: absolute; left: 528px; top: 238px; font-family: "Nunito", sans-serif; font-weight: 600; color: var(--green); font-size: 42px; line-height: 42px; }

  .team { position: absolute; left: 442px; top: 390px; width: 316px; }
  .team__title { font-family: "Shadows Into Light Two", cursive; color: var(--grey); font-size: 44px; line-height: 42px; font-weight: 400; margin-bottom: 10px; }
  .team .body-copy p { text-align: left; font-size: 19.5px; line-height: 27.5px; }

  .promise { position: absolute; left: 41px; top: 735px; width: 720px; height: 152px; }
  .promise__mark { position: absolute; left: 6px; top: 44px; width: 96px; height: 96px; border-radius: 50%; background: var(--navy); }
  .promise__text { position: absolute; left: 137px; top: 28px; font-family: "Nunito", sans-serif; font-weight: 600; color: var(--navy); font-size: 32px; line-height: 43px; }

  .privacy { position: absolute; left: 843px; top: 103px; width: 315px; }
  .privacy__title { font-family: "Nunito", sans-serif; font-weight: 600; color: var(--navy); font-size: 42px; line-height: 45px; margin-bottom: 12px; }
  .privacy .body-copy p { line-height: 27.5px; }
</style>
</head>
<body>
<main class="spread">
  <div class="band band--top"></div>
  <div class="band band--bottom"></div>
  <div class="tab tab--top"></div>
  <div class="tab tab--bottom"></div>

  <section class="about">
    <h2 class="about__label">Who we are</h2>
    <div class="body-copy">
      <p>Since our founding over 25 years ago, Kestrel has successfully placed thousands of technical people in hundreds of the best companies.</p>
      <p>Our prestigious portfolio of clients includes the most promising tech startups and Fortune 100 companies.</p>
      <p>We specialize in connecting the most sought after finance technology and web development talent.</p>
      <p>We recruit all levels of experience, from the best university computer science graduates to candidates who have attained the highest levels of technology management and accomplishment.</p>
    </div>
  </section>

  <div class="art art--bubbles" role="img" aria-label="Cluster of linked speech bubbles naming programming languages"></div>
  <div class="art art--figure" role="img" aria-label="Cartoon recruiter figure with glasses and tie"></div>
  <p class="tagline">we speak<br>your language</p>

  <section class="team">
    <h2 class="team__title">Our entire team<br>knows your name</h2>
    <div class="body-copy">
      <p>Our recruiters work as a team. No need to use multiple firms when you have the resources of the entire Kestrel team working for you. And get this, when you call you will not be subjected to voicemail; you always speak to a person.</p>
    </div>
  </section>

  <section class="promise">
    <div class="promise__mark"></div>
    <p class="promise__text">Technology will always change,<br>but you can expect Kestrel's high<br>level of service to remain the same.</p>
  </section>

  <section class="privacy">
    <h2 class="privacy__title">Confidentiality<br>is a priority</h2>
    <div class="body-copy">
      <p>In this era where information access has greatly improved our lives, it has also increased the potential for misuse.</p>
      <p>At Kestrel, we strive to provide the highest level of confidentiality for both our clients and candidates.</p>
      <p>We work on an exclusive basis so we can assure our clients and candidates individualized attention and privacy.</p>
      <p>We do not publicly share the names or private data of our clients or candidates in social media or on our website.</p>
      <p>Candidates can trust their careers in our hands since we will not mass mail their resumes or release any information without their approval.</p>
    </div>
  </section>
</main>
</body>
</html>
```